Healthy Supplement featuring Moringa products

Need 3 business card options for our reps to order from Printwell. Our reps will be ordering from Printwell once we upload them. Attached is our current designs to show what info needs to be on the cards. Our website is www.tqvitality.com
The business cards will be a template for our reps to order from. Most of our reps are Asian & Hispanic. Please look at our website so you can see who we are to get the look and feel what we need.
Target Market(s)
Adults 30 on up. Health oriented people.
Industry/Entity Type
Health And Wellness
Contact Information for Business Card
Name
Title
Phone
Logo
www.tqvitality.com/my/username
Font styles to use
Requirements
Must have
- Please match our website look and colors. A moringa leaf is nice, but am open to something different.
Nice to have
- Healthy looking and warm, not super cold or too modern.
Should not have
- No harsh colors please.

```html
<!DOCTYPE html>
<html lang="en">
<head>
<meta charset="utf-8">
<title>TQ Vitality Business Card</title>
<link rel="stylesheet" href="https://fonts.googleapis.com/css2?family=Roboto:wght@400;500;700&display=swap">
<style>
  :root {
    --backdrop-light: #8e989c;
    --backdrop-dark: #3f484c;
    --card-white: #ffffff;
    --leaf-green: #6aa842;
    --lime-green: #8dc63f;
    --deep-green: #4f8f2c;
    --text-white: #ffffff;
  }
  * { box-sizing: border-box; margin: 0; padding: 0; }
  html, body { width: 1200px; height: 900px; overflow: hidden; }
  body {
    background: radial-gradient(ellipse at 50% 45%, var(--backdrop-light), var(--backdrop-dark) 80%);
    font-family: "Roboto", Arial, sans-serif;
    position: relative;
  }
  .card {
    position: absolute;
    width: 520px;
    height: 297px;
    background: var(--card-white);
    overflow: hidden;
    box-shadow: 0 12px 28px rgba(0,0,0,.35);
  }
  .card--front { left: 50px; top: 140px; }
  .card--back { left: 630px; top: 460px; }
  .card__waves { position: absolute; inset: 0; width: 100%; height: 100%; }

  .brand {
    position: absolute;
    display: flex;
    align-items: center;
    gap: 10px;
    color: var(--leaf-green);
    font-weight: 700;
    font-size: 34px;
    letter-spacing: 1px;
    white-space: nowrap;
  }
  .brand__dot {
    width: 30px; height: 30px;
    border-radius: 50%;
    background: var(--leaf-green);
  }
  .card--front .brand { left: 150px; top: 78px; }
  .card--back .brand { left: 40px; top: 95px; }

  .front__web {
    position: absolute;
    left: 34px; bottom: 28px;
    color: var(--text-white);
    font-size: 14px;
  }

  .holder {
    position: absolute;
    right: 36px; top: 28px;
    text-align: right;
    color: var(--leaf-green);
  }
  .holder__name { font-weight: 700; font-size: 18px; letter-spacing: .5px; }
  .holder__title { font-weight: 700; font-size: 9px; color: var(--lime-green); }

  .contact {
    position: absolute;
    right: 28px; top: 118px;
    list-style: none;
    color: var(--text-white);
    font-size: 12.5px;
    text-align: right;
  }
  .contact li { display: flex; justify-content: flex-end; align-items: center; gap: 8px; line-height: 20px; }
  .contact svg { width: 11px; height: 11px; fill: var(--text-white); flex: none; }

  .address {
    position: absolute;
    left: 150px; bottom: 16px;
    color: var(--text-white);
    font-size: 13px;
    line-height: 17px;
  }
</style>
</head>
<body>

<section class="card card--front">
  <svg class="card__waves" viewBox="0 0 520 297" preserveAspectRatio="none" aria-hidden="true">
    <path d="M0,225 C120,190 260,180 340,165 C420,150 470,110 520,75 L520,297 L0,297 Z" fill="var(--leaf-green)"/>
    <path d="M330,163 C420,142 475,100 520,60 L520,75 C470,110 420,150 340,168 Z" fill="var(--lime-green)"/>
    <path d="M300,160 C400,140 460,110 510,72" stroke="var(--card-white)" stroke-width="3" fill="none"/>
    <path d="M70,255 C170,210 290,193 380,178" stroke="var(--lime-green)" stroke-width="1.5" fill="none" opacity=".8"/>
  </svg>
  <div class="brand"><span class="brand__dot"></span>TQ Vitality</div>
  <p class="front__web">www.yourweb.com</p>
</section>

<section class="card card--back">
  <svg class="card__waves" viewBox="0 0 520 297" preserveAspectRatio="none" aria-hidden="true">
    <path d="M0,222 C120,219 200,210 250,165 C300,112 400,80 520,58 L520,297 L0,297 Z" fill="var(--leaf-green)"/>
    <path d="M240,172 C295,110 395,74 520,48 L520,58 C400,80 300,112 250,165 Z" fill="var(--lime-green)"/>
    <path d="M270,145 C330,100 420,78 500,65" stroke="var(--lime-green)" stroke-width="1.5" fill="none"/>
    <path d="M30,230 C140,227 205,216 250,180" stroke="var(--lime-green)" stroke-width="1.5" fill="none"/>
    <path d="M40,238 C150,235 215,223 262,190" stroke="var(--card-white)" stroke-width="3" fill="none"/>
  </svg>
  <svg class="card__waves" viewBox="0 0 520 297" preserveAspectRatio="none" role="img" aria-label="Faint moringa leaf sprig decoration">
    <ellipse cx="300" cy="198" rx="58" ry="16" fill="var(--card-white)" opacity=".14"/>
  </svg>
  <div class="brand"><span class="brand__dot"></span>TQ Vitality</div>
  <div class="holder">
    <p class="holder__name">JOHN SMITH</p>
    <p class="holder__title">OWNER</p>
  </div>
  <ul class="contact">
    <li>123-456-1234
      <svg viewBox="0 0 24 24"><path d="M6.6 10.8a15 15 0 0 0 6.6 6.6l2.2-2.2a1 1 0 0 1 1-.25 11 11 0 0 0 3.6.6 1 1 0 0 1 1 1V20a1 1 0 0 1-1 1A17 17 0 0 1 3 4a1 1 0 0 1 1-1h3.5a1 1 0 0 1 1 1 11 11 0 0 0 .6 3.6 1 1 0 0 1-.25 1z"/></svg></li>
    <li>123-456-1234
      <svg viewBox="0 0 24 24"><path d="M3 8c0-2 4-4 9-4s9 2 9 4v2h-5V8H8v2H3z M5 12h14l1 8H4z"/></svg></li>
    <li>yourmaail@email.com
      <svg viewBox="0 0 24 24"><path d="M2 5h20v14H2z M3 6l9 7 9-7" stroke="#6aa842" stroke-width="1.5"/></svg></li>
    <li>www.yourweb.com
      <svg viewBox="0 0 24 24"><circle cx="12" cy="12" r="10"/><path d="M2 12h20M12 2c3 3 3 17 0 20M12 2c-3 3-3 17 0 20" stroke="#6aa842" stroke-width="1.5" fill="none"/></svg></li>
  </ul>
  <p class="address">Level 2 Harbour View Plaza<br>Reed Street, Suva, Fiji</p>
</section>

</body>
</html>
```